Rota sem falha

We need a web design for a new company based in João Pessoa, Brazil, called Rota Sem Falha (Smooth Route). After the client/consumer fullfill a questionary about the wanted destination, personal interests and available budget for the trip, we aim to plan a personalized travel guide for that independent travellers, containing informations about the places we suggest them to visit, amount of days indicated in each city, possibles restaurants and hotels. The site will help people to manage their budgets and optimize the time at their travel at a low cost and in a simple way. We would like to see clean and sophisticated design that use colors in shades of black, grey and white (and perhaps a touch of pink - what do you think?). The final design should communicate safety, professionalism and experience.
Updates
Target Market(s)
People who dont like to buy excursion packages but think they could need a consultance in planning their trip
Industry/Entity Type
It Company
Requirements
Must have
- The menu shall indicate the following points (that will lead to new pages):
1-Our Services
2-Prices
2- FAQ
3-Hire a travel expert to plan your trip!
4-Around the world - blog
Fell free to put the logo of the site "Rota Sem Falha" in the top middle/top left/ or wherever you find it is more appropriate.
On the top right we should put a login/register button.
Above that menu, I thought about illustrating with a figure demonstrating how it works - step by step, as seen in the link http://trekvolo.example/ - but in a more clean design.
Nice to have
- Quik coin will be used as the payment option.

```html
<!DOCTYPE html>
<html lang="en">
<head>
<meta charset="utf-8">
<title>Rota Sem Falha</title>
<link href="https://fonts.googleapis.com/css2?family=Ubuntu:ital,wght@0,400;0,500;0,700;1,300;1,400&family=Arimo:wght@400;700&display=swap" rel="stylesheet">
<style>
:root{
  --pink:#ee2c8c;
  --pink-soft:#e9529b;
  --ink:#111;
  --text:#222;
  --page:#efefef;
  --bar-top:#4a4a4a;
  --bar-bottom:#0b0b0b;
  --grey:#8a8a8a;
  --white:#fff;
}
*{box-sizing:border-box;margin:0;padding:0}
html,body{width:1107px;height:1200px;overflow:hidden}
body{position:relative;background:var(--page);font-family:"Arimo",Arial,sans-serif;color:var(--text)}
.abs{position:absolute}

/* header */
.brand{left:118px;top:34px;font-family:"Ubuntu",sans-serif;font-weight:700;font-size:38px;color:var(--pink);letter-spacing:-.5px;line-height:1}
.social{top:66px;display:flex;gap:6px;left:639px}
.social span{width:30px;height:30px;border-radius:50%;background:radial-gradient(circle at 40% 35%,#3a3f4d,#050608);box-shadow:0 1px 2px rgba(0,0,0,.5)}
.btn-small{top:66px;height:30px;border-radius:5px;background:linear-gradient(#3a3a3a,#050505);color:var(--white);font-size:13px;display:flex;align-items:center;justify-content:center;border:1px solid #000}
.btn-login{left:832px;width:72px}
.btn-register{left:918px;width:72px}

/* navigation */
.main-nav{left:0;top:121px;width:1107px;height:44px;background:linear-gradient(var(--bar-top),var(--bar-bottom) 55%,#1a1a1a)}
.main-nav ul{list-style:none;display:flex;align-items:center;height:100%;font-size:13.5px;color:var(--white)}
.main-nav li{position:absolute;top:0;height:44px;line-height:44px}
.main-nav .active{background:var(--pink);width:89px;text-align:center}

/* slider */
.slider{left:106px;top:183px;width:893px;height:313px;background:var(--white);padding:4px;box-shadow:0 14px 14px -10px rgba(0,0,0,.25)}
.slide-img{width:885px;height:305px;position:relative;background:linear-gradient(180deg,#5b4f8e 0%,#c9679c 22%,#c7708c 30%,#1a1420 52%,#0c0a10 72%,#2a1a2a 100%)}
.arrow{position:absolute;top:140px;width:24px;height:24px;border-radius:50%;background:#eee}
.caption{position:absolute;left:0;bottom:0;width:100%;height:43px;background:rgba(0,0,0,.78)}
.caption p{position:absolute;right:16px;top:8px;font-family:"Ubuntu",sans-serif;font-style:italic;font-weight:300;font-size:23px;color:var(--white)}
.caption p em{color:var(--pink-soft);font-style:italic}
.dots{position:absolute;left:28px;top:17px;display:flex;gap:8px}
.dots span{width:13px;height:13px;border-radius:50%;background:#8d8d8d}
.dots .on{background:var(--pink)}

/* about */
.section-title{font-family:"Ubuntu",sans-serif;font-size:22px;color:var(--pink-soft);font-weight:400}
.about-title{left:111px;top:544px}
.about-text{left:112px;top:582px;width:585px;font-size:10.8px;line-height:16.6px;text-align:justify}
.video{left:729px;top:550px;width:265px;height:178px;background:var(--white);border:1px solid #ddd;padding:3px}
.video-img{width:100%;height:100%;background:linear-gradient(120deg,#e8e8ea 0%,#c9ccd3 35%,#6c7fa5 55%,#e7e2df 100%);display:flex;align-items:center;justify-content:center}
.play{width:48px;height:48px;border-radius:50%;background:rgba(40,40,40,.75);border:3px solid rgba(255,255,255,.7);position:relative}
.play::after{content:"";position:absolute;left:17px;top:12px;border-left:16px solid #fff;border-top:10px solid transparent;border-bottom:10px solid transparent}
.plan-title{left:111px;top:707px}

/* steps */
.step{top:753px;width:172px;height:172px;border-radius:50%;background:var(--white);border:4px solid #f4f4f4;box-shadow:0 0 4px rgba(0,0,0,.18);text-align:center}
.step h3{font-family:"Ubuntu",sans-serif;font-style:italic;font-weight:400;font-size:18px;color:var(--pink-soft);margin-top:24px}
.step p{font-size:12.3px;margin-top:6px}
.step svg{margin-top:14px}
.step .btn-go{margin:20px auto 0;width:124px;height:34px;border-radius:10px;background:linear-gradient(#3a3a3a,#050505);color:var(--white);font-family:"Ubuntu",sans-serif;font-size:12.5px;line-height:34px}
.step-note{top:949px;width:170px;text-align:center;font-size:11.5px;line-height:16.6px}

/* call to action */
.cta-line{left:160px;top:1055px;width:790px;height:1px;background:linear-gradient(90deg,transparent,#bdbdbd 20%,#bdbdbd 80%,transparent)}
.cta{left:412px;top:1031px;width:282px;height:47px;border-radius:24px;background:linear-gradient(#3c3c3c,#040404);color:var(--white);font-family:"Ubuntu",sans-serif;font-size:22px;text-align:center;line-height:47px;box-shadow:0 1px 2px rgba(0,0,0,.4)}

/* footer */
.footer{left:0;top:1107px;width:1107px;height:93px;background:#0d0d0d;color:var(--white)}
.footer-links{position:absolute;left:95px;top:28px;font-size:11.6px;white-space:nowrap}
.footer-links span{margin-right:12px}
.copyright{position:absolute;left:93px;top:57px;font-size:11.6px}
.badge{position:absolute;left:798px;top:14px;width:60px;height:60px;border-radius:50%;background:radial-gradient(circle at 40% 35%,#fff1a0,#e0b830);border:2px solid #c8a020}
.pay-name{position:absolute;left:900px;top:10px;font-family:"Ubuntu",sans-serif;font-weight:700;font-size:21px;color:#6fa6e0}
.cards{position:absolute;left:872px;top:48px;display:flex;gap:4px}
.cards span{width:31px;height:20px;border-radius:2px;background:#dcdcdc}
</style>
</head>
<body>

<header>
  <div class="abs brand">Rota Sem Falha</div>
  <div class="abs social" aria-label="Social links"><span></span><span></span><span></span></div>
  <div class="abs btn-small btn-login">Login</div>
  <div class="abs btn-small btn-register">Register</div>
</header>

<nav class="abs main-nav">
  <ul>
    <li class="active" style="left:107px">Home</li>
    <li style="left:205px">|</li>
    <li style="left:238px">Our Services</li>
    <li style="left:341px">|</li>
    <li style="left:380px">Price</li>
    <li style="left:442px">|</li>
    <li style="left:481px">FAQ</li>
    <li style="left:540px">|</li>
    <li style="left:583px">Hire a travel expert to plan your trip</li>
    <li style="left:820px">|</li>
    <li style="left:856px">Around the world - blog</li>
  </ul>
</nav>

<section class="abs slider">
  <div class="slide-img" role="img" aria-label="Night view of a riverside city with illuminated bridge and tower under a pink sky">
    <svg class="arrow" style="left:18px" viewBox="0 0 24 24"><path d="M14 7l-5 5 5 5" fill="none" stroke="#333" stroke-width="2.5"/></svg>
    <svg class="arrow" style="right:18px" viewBox="0 0 24 24"><path d="M10 7l5 5-5 5" fill="none" stroke="#333" stroke-width="2.5"/></svg>
    <div class="caption">
      <div class="dots"><span></span><span></span><span class="on"></span><span></span></div>
      <p>Plan Your Trip with our <em>Expert Consultants!</em></p>
    </div>
  </div>
</section>

<h2 class="abs section-title about-title">Who We Are</h2>
<p class="abs about-text">Lorem Ipsum is simply dummy text of the printing and typesetting industry. Lorem Ipsum has been the industry's standard dummy text ever since the 1500s, when an unknown printer took a galley of type and scrambled it to make a type specimen book. It has survived not only five centuries, but also the leap into electronic typesetting, remaining essentially unchanged. It was popularised Lorem Ipsum is simply dummy text of the printing and typesetting industry. Lorem Ipsum specimen book. It has survived not only five centuries, but also the leap into electronic typesetting, remaining essentially unchanged. It was popularised Lorem Ipsum is simply dummy text of the printing and typesetting industry. Lorem Ipsum</p>
<div class="abs video"><div class="video-img" role="img" aria-label="Video still of a travel consultant talking with a family on a sofa"><div class="play"></div></div></div>

<h2 class="abs section-title plan-title">Plan a Smart Ltinerary</h2>

<div class="abs step" style="left:99px">
  <h3>Generate</h3><p>your personal trip plan</p>
  <div class="btn-go">Get Started Now</div>
</div>
<div class="abs step" style="left:281px">
  <h3>Review</h3><p>the suggested itinerary</p>
  <svg width="84" height="34" viewBox="0 0 84 34"><g fill="#9a9a9a"><path d="M10 14l3 6 6 1-4 4 1 6-6-3-6 3 1-6-4-4 6-1z"/><path d="M74 14l3 6 6 1-4 4 1 6-6-3-6 3 1-6-4-4 6-1z"/><path d="M24 10l3.5 7 7.5 1-5.5 5 1.5 7.5-7-3.5-7 3.5 1.5-7.5-5.5-5 7.5-1z"/><path d="M60 10l3.5 7 7.5 1-5.5 5 1.5 7.5-7-3.5-7 3.5 1.5-7.5-5.5-5 7.5-1z"/><path d="M42 2l4.5 9 9.5 1.5-7 6.5 2 9.5-9-4.5-9 4.5 2-9.5-7-6.5 9.5-1.5z" fill="#7a7a7a"/></g></svg>
</div>
<div class="abs step" style="left:465px">
  <h3>Refine</h3><p>just about everything</p>
  <svg width="50" height="46" viewBox="0 0 50 46"><path d="M5 16L25 4l20 12v28H5z" fill="none" stroke="#888" stroke-width="2.5"/><rect x="14" y="18" width="22" height="16" fill="none" stroke="#888" stroke-width="2"/><circle cx="25" cy="26" r="4" fill="none" stroke="#888" stroke-width="2"/><rect x="19" y="37" width="12" height="3" fill="#888"/></svg>
</div>
<div class="abs step" style="left:645px">
  <h3>Compare</h3><p>hotel prices and book</p>
  <svg width="60" height="46" viewBox="0 0 60 46"><rect x="26" y="6" width="8" height="32" fill="#888"/><rect x="10" y="38" width="40" height="6" rx="2" fill="#777"/><rect x="8" y="18" width="44" height="4" fill="#888"/><rect x="4" y="24" width="16" height="10" rx="3" fill="#999"/><rect x="40" y="24" width="16" height="10" rx="3" fill="#999"/><circle cx="30" cy="6" r="5" fill="#777"/></svg>
</div>
<div class="abs step" style="left:829px">
  <h3>Print</h3><p>your plan and bon voyage</p>
  <svg width="56" height="46" viewBox="0 0 56 46"><rect x="16" y="2" width="24" height="12" fill="#888"/><rect x="3" y="12" width="50" height="20" rx="3" fill="#777"/><rect x="14" y="22" width="28" height="22" fill="#fff" stroke="#777" stroke-width="2"/><g stroke="#888" stroke-width="2"><line x1="18" y1="29" x2="38" y2="29"/><line x1="18" y1="34" x2="38" y2="34"/><line x1="18" y1="39" x2="38" y2="39"/></g><circle cx="47" cy="19" r="2" fill="#ccc"/></svg>
</div>

<p class="abs step-note" style="left:101px">Simply click the get started button and follow the wizard</p>
<p class="abs step-note" style="left:278px">Attractions, places to eat, hotel, schedule and even directions</p>
<p class="abs step-note" style="left:468px">For each change, your trip will be optimized to fit your every whim!</p>
<p class="abs step-note" style="left:647px">Find your hotel, and we'll link you to the supplier of your choice</p>
<p class="abs step-note" style="left:833px">After all, travel advice this great shouldn't be left at home!</p>

<div class="abs cta-line"></div>
<div class="abs cta">Get Started Now</div>

<footer class="abs footer">
  <div class="footer-links"><span>Home</span><span>|</span><span>Our Services</span><span>|</span><span>Price</span><span>|</span><span>FAQ</span><span>|</span><span>Hire a travel expert to plan your trip</span><span>|</span><span>Around the world - blog</span></div>
  <div class="copyright">Copyright © Rota Sem Falha &nbsp;&nbsp;2013 &nbsp;All Rights Reserved</div>
  <div class="badge"></div>
  <div class="pay-name">Quik coin</div>
  <div class="cards"><span></span><span></span><span></span><span></span></div>
</footer>

</body>
</html>
```